Business Card Design

Company is a Commercial Building Company specialising in New Construction and existing refurbishments

Industry/Entity Type

Business

Contact Information for Business Card

Dale Mercer
Construction Manager
E Dale@harbridgebuilding.com.au
M 0400 213 947
Mail 27 Tarrant Rise Fernhaven WA 6214

```html
<!DOCTYPE html>
<html lang="en">
<head>
<meta charset="utf-8">
<title>Harbridge Building &amp; Construction – Business Card</title>
<link rel="stylesheet" href="https://fonts.googleapis.com/css2?family=Arimo:wght@400;700&display=swap">
<style>
  :root {
    --backdrop: #e9e6e1;
    --slate: #5b5e6b;
    --orange: #f7891f;
    --cyan: #1fb5d6;
    --white: #ffffff;
    --paper: #f7f8fa;
    --ink: #4a4d58;
  }
  * { box-sizing: border-box; margin: 0; padding: 0; }
  html, body {
    width: 1200px; height: 870px; overflow: hidden;
    background: var(--backdrop);
    font-family: "Arimo", Arial, sans-serif;
  }
  .canvas { position: relative; width: 1200px; height: 870px; }
  .card {
    position: absolute; top: 105px;
    width: 400px; height: 660px;
    overflow: hidden;
    box-shadow: 0 6px 22px rgba(0,0,0,.18);
  }
  .card--front { left: 170px; background: var(--slate); color: var(--white); }
  .card--back { left: 630px; background: var(--paper); }

  .brand {
    position: absolute; top: 78px; left: 0; right: 0;
    display: flex; flex-direction: column; align-items: center; gap: 14px;
  }
  .brand__mark { width: 30px; height: 30px; background: var(--orange); }
  .brand__name {
    font-weight: 700; font-size: 24px; letter-spacing: 1.5px;
    text-align: center; line-height: 1.2; text-transform: uppercase;
    color: var(--white);
  }
  .person { position: absolute; top: 232px; left: 0; right: 0; text-align: center; }
  .person__name { font-size: 44px; color: var(--orange); font-weight: 400; letter-spacing: .5px; }
  .person__role { font-size: 15px; margin-top: 4px; letter-spacing: .3px; }
  .contact {
    position: absolute; top: 340px; left: 0; right: 0;
    text-align: center; font-size: 17px; line-height: 1.45; list-style: none;
  }
  .card__photo { position: absolute; left: 0; bottom: 0; width: 400px; height: 660px; }

  .backdrop-photo { position: absolute; inset: 0; width: 100%; height: 100%; }
  .card--back .brand { top: 430px; }
  .card--back .brand__name { color: var(--ink); }
  .card--back .brand__mark { background: var(--cyan); }
</style>
</head>
<body>
<main class="canvas">

  <section class="card card--front" aria-label="Business card front">
    <div class="brand">
      <span class="brand__mark"></span>
      <p class="brand__name">Harbridge Building<br>&amp; Construction</p>
    </div>
    <div class="person">
      <h1 class="person__name">Dale Mercer</h1>
      <p class="person__role">Construction Manager</p>
    </div>
    <ul class="contact">
      <li>0400 213 947</li>
      <li>Dale@harbridgebuilding.com.au</li>
      <li>27 Tarrant Rise Fernhaven WA 6214</li>
    </ul>
    <svg class="card__photo" viewBox="0 0 400 660">
      <defs>
        <linearGradient id="patioTones" x1="0" y1="0" x2="0" y2="1">
          <stop offset="0" stop-color="#b9a58a"/>
          <stop offset=".45" stop-color="#d9d8d2"/>
          <stop offset=".75" stop-color="#c7c9c4"/>
          <stop offset="1" stop-color="#5f9a3c"/>
        </linearGradient>
      </defs>
      <path role="img" aria-label="Photo of a finished outdoor patio with timber pergola, stone steps and lawn"
            d="M0 572 C 110 470, 250 560, 400 400 L400 660 L0 660 Z" fill="url(#patioTones)"/>
      <path d="M0 572 C 110 470, 250 560, 400 400" fill="none" stroke="var(--orange)" stroke-width="7"/>
    </svg>
  </section>

  <section class="card card--back" aria-label="Business card back">
    <svg class="backdrop-photo" viewBox="0 0 400 660">
      <defs>
        <linearGradient id="towerTones" x1="0" y1="0" x2="1" y2="1">
          <stop offset="0" stop-color="#ffffff"/>
          <stop offset=".5" stop-color="#e4e5ea"/>
          <stop offset="1" stop-color="#d3d5dc"/>
        </linearGradient>
      </defs>
      <rect role="img" aria-label="Faded photo of a multi-storey apartment building with balconies"
            width="400" height="660" fill="url(#towerTones)"/>
    </svg>
    <div class="brand">
      <span class="brand__mark"></span>
      <p class="brand__name">Harbridge Building<br>&amp; Construction</p>
    </div>
  </section>

</main>
</body>
</html>
```